Update Dulmar & Co Powerpoint to Quillmere Partnership

Hi, about 2 years ago I had a great Powerpoint template produced for my business called Dulmar & Co. We have now changed the company name and logo to Quillmere Partnership and I would like you to update the presentation template pages to the new logo and design.

I attach:

1) The original Powerpoint presentation that was produced for Dulmar
2) The new Quillmere Partnership logo files
3) The initial Powerpoint presentation format that my UK designer has done to give you an idea of their approach
4) The Font files (Red Hat Display - medium)

It would be great to receive the new PP template by Tuesday 22nd July.

Please message me if you have any questions.
Thanks
Ned

```html
<!DOCTYPE html>
<html lang="en">
<head>
<meta charset="utf-8">
<title>Quillmere Partnership – Presentation Template Overview</title>
<link rel="stylesheet" href="https://fonts.googleapis.com/css2?family=Red+Hat+Display:ital,wght@0,400;0,500;0,700;0,800;0,900;1,500&display=swap">
<style>
:root{
  --teal:#163a3f;
  --teal-2:#1f4a50;
  --orange:#e8561c;
  --gray:#c7cbcd;
  --ink:#243033;
  --mute:#8d9597;
  --bg:#dcdfe1;
  --white:#ffffff;
}
*{box-sizing:border-box;margin:0;padding:0}
html,body{width:785px;height:1200px;overflow:hidden}
body{position:relative;background:var(--bg);font-family:'Red Hat Display',sans-serif;color:var(--ink)}
.icon-defs{position:absolute;width:0;height:0;overflow:hidden}
.ic{display:block;fill:none;stroke:currentColor;stroke-width:1.8;stroke-linecap:round;stroke-linejoin:round}
.slide{position:absolute;width:231px;height:130px;background:var(--white);overflow:hidden;box-shadow:0 1px 3px rgba(0,0,0,.18)}
.slide>*{position:absolute}
.slide.dark{background:var(--teal)}
.dark-photo{inset:0;background:radial-gradient(circle at 30% 40%,#24484d,#163a3f 60%,#112f33)}
.heading{left:7px;top:7px;font-size:8px;font-weight:500;line-height:1;white-space:nowrap}
.heading b{font-weight:800}
.heading::after{content:"";position:absolute;left:0;top:11px;width:14px;height:1.6px;background:var(--orange)}
.brand{right:8px;top:6px;display:flex;align-items:center;gap:2px}
.brand .mark{width:4px;height:4px;background:var(--orange)}
.brand .name{font-size:4.6px;font-weight:800;line-height:.95;color:var(--ink)}
.brand .name small{display:block;font-size:1.9px;letter-spacing:.35px}
.foot{left:7px;right:7px;bottom:6px;height:5px;border-bottom:.5px solid var(--teal);display:flex;justify-content:space-between;align-items:flex-end;font-size:1.7px;color:var(--ink)}
.foot .pg{font-size:2.6px;transform:translateY(3.5px)}
.t{font-size:2.5px;line-height:1.45;color:var(--mute)}
.t.dk{color:var(--ink)}
.h5{font-size:4px;font-weight:700;line-height:1.2;color:var(--ink)}
.o{color:var(--orange)}
.w{color:var(--white)}
.photo{background:linear-gradient(140deg,#6f7f88,#b9c2c6 55%,#e2e5e6)}
.photo.warm{background:linear-gradient(140deg,#4c5b63,#9aa5aa 55%,#d6cdc2)}
.round{border-radius:3px}
.tile{background:var(--teal);border-radius:2px;padding:3px;color:var(--white)}
.tile .h5{color:var(--orange);font-size:3.2px;margin-top:2px}
.tile .t{color:#d7dfe0;font-size:2.1px}
.ring{border-radius:50%;border:1px solid var(--orange);display:flex;align-items:center;justify-content:center;color:var(--orange);background:var(--white)}
.num{width:9px;height:9px;border-radius:50%;display:flex;align-items:center;justify-content:center;color:var(--white);font-size:4.5px;font-weight:800}
.toc-row{display:flex;align-items:center;gap:2px;width:88px;font-size:2.9px;font-weight:500;color:var(--ink)}
.toc-row::before{content:"";width:1.6px;height:1.6px;border-radius:50%;background:var(--orange)}
.toc-row .line{flex:1;height:0;border-bottom:.4px solid var(--mute);margin:0 2px}
.toc-row .n{width:6px;height:6px;border-radius:50%;background:var(--teal);color:var(--white);font-size:2.3px;font-weight:700;display:flex;align-items:center;justify-content:center}
.part-no{font-size:32px;font-weight:900;line-height:1}
.part-title{font-size:10px;font-weight:800;color:var(--orange);line-height:1}
.brand-big .name{font-size:7.6px;font-weight:800;line-height:.9;color:var(--white)}
.brand-big .name small{display:block;font-size:2.6px;letter-spacing:.6px}
.bullet{font-size:4px;font-weight:500;color:var(--ink);display:flex;gap:2px;align-items:center}
.bullet::before{content:"";width:1.8px;height:1.8px;border-radius:50%;background:var(--orange)}
.phone-frame{border:.8px solid var(--ink);border-radius:3px;background:var(--white);padding:5px 3px}
.feature-box{width:17px;height:17px;margin:0 auto 3px;display:flex;align-items:center;justify-content:center}
.feature-box.line{border:1.2px solid var(--teal);color:var(--teal);background:#fff}
.feature-box.fill{background:var(--orange);color:#fff}
.team-card{width:34px;text-align:center}
.team-card .bar{height:11px}
.team-card .avatar{width:17px;height:17px;border-radius:50%;margin:-8px auto 0;border:1px solid var(--white);background:linear-gradient(160deg,#cbbcae,#8a7566)}
.team-card .h5{font-size:3.3px;color:var(--orange);margin-top:3px}
.team-card .h5.dk{color:var(--ink)}
.contact{display:flex;gap:4px;align-items:flex-start;font-size:3.6px;line-height:1.25;color:var(--white)}
.contact svg{flex:none}
.contact span{border-left:.5px solid var(--white);padding-left:2px}
</style>
</head>
<body>

<svg class="icon-defs" aria-hidden="true">
  <symbol id="i-users" viewBox="0 0 24 24"><circle cx="9" cy="8" r="3"/><circle cx="16.5" cy="9" r="2.5"/><path d="M3 19c0-4.5 12-4.5 12 0M14 18c1-3 7-3 7 0"/></symbol>
  <symbol id="i-user" viewBox="0 0 24 24"><circle cx="12" cy="7" r="3.5"/><path d="M5 21c0-6.5 14-6.5 14 0"/></symbol>
  <symbol id="i-heart" viewBox="0 0 24 24"><path d="M12 20 5 13a4 4 0 0 1 7-5 4 4 0 0 1 7 5z"/></symbol>
  <symbol id="i-bulb" viewBox="0 0 24 24"><path d="M9 17h6M10 20h4M12 3a6 6 0 0 1 3 11v2H9v-2a6 6 0 0 1 3-11"/></symbol>
  <symbol id="i-mail" viewBox="0 0 24 24"><rect x="3" y="6" width="18" height="12" rx="1"/><path d="m3 7 9 6 9-6"/></symbol>
  <symbol id="i-chart" viewBox="0 0 24 24"><path d="M4 20h16M7 17v-4M12 17V8M17 17v-6"/></symbol>
  <symbol id="i-growth" viewBox="0 0 24 24"><path d="M4 20h16M5 15l5-5 3 3 6-6M15 7h4v4"/></symbol>
  <symbol id="i-target" viewBox="0 0 24 24"><circle cx="12" cy="12" r="8"/><circle cx="12" cy="12" r="4"/><circle cx="12" cy="12" r="1"/></symbol>
  <symbol id="i-search" viewBox="0 0 24 24"><circle cx="10" cy="10" r="6"/><path d="m15 15 5 5"/></symbol>
  <symbol id="i-clock" viewBox="0 0 24 24"><circle cx="12" cy="12" r="8"/><path d="M12 7v5l3 2"/></symbol>
  <symbol id="i-coin" viewBox="0 0 24 24"><circle cx="12" cy="12" r="8"/><path d="M12 6.5v11M14.5 9h-3.5a1.5 1.5 0 0 0 0 3h2a1.5 1.5 0 0 1 0 3H9.5"/></symbol>
  <symbol id="i-db" viewBox="0 0 24 24"><ellipse cx="12" cy="6" rx="7" ry="2.5"/><path d="M5 6v12a7 2.5 0 0 0 14 0V6M5 12a7 2.5 0 0 0 14 0"/></symbol>
  <symbol id="i-flag" viewBox="0 0 24 24"><path d="M6 21V4h11l-2 4 2 4H6"/></symbol>
  <symbol id="i-eye" viewBox="0 0 24 24"><path d="M2 12s4-7 10-7 10 7 10 7-4 7-10 7S2 12 2 12z"/><circle cx="12" cy="12" r="3"/></symbol>
  <symbol id="i-rocket" viewBox="0 0 24 24"><path d="M12 3c4 3 5 8 3 13H9C7 11 8 6 12 3zM9 16l-3 4M15 16l3 4"/><circle cx="12" cy="10" r="1.5"/></symbol>
  <symbol id="i-pen" viewBox="0 0 24 24"><path d="m4 20 4-1L19 8l-3-3L5 16z"/></symbol>
  <symbol id="i-book" viewBox="0 0 24 24"><rect x="4" y="4" width="16" height="16" rx="1"/><path d="M12 4v16M7 9h3M14 9h3M7 13h3M14 13h3"/></symbol>
  <symbol id="i-gear" viewBox="0 0 24 24"><circle cx="12" cy="12" r="3"/><path d="M12 3v3M12 18v3M3 12h3M18 12h3M5.6 5.6l2.1 2.1M16.3 16.3l2.1 2.1M5.6 18.4l2.1-2.1M16.3 7.7l2.1-2.1"/></symbol>
  <symbol id="i-down" viewBox="0 0 24 24"><path d="M4 4v16h16M7 8l5 6 3-3 4 5"/></symbol>
  <symbol id="i-award" viewBox="0 0 24 24"><circle cx="12" cy="9" r="5"/><path d="m9 13-2 8 5-3 5 3-2-8"/></symbol>
</svg>

<!-- Row 1 -->
<section class="slide dark" style="left:35px;top:33px" aria-label="Cover">
  <div class="brand-big" style="left:13px;top:16px;display:flex;gap:3px;align-items:center">
    <div style="width:6px;height:6px;background:var(--orange)"></div>
    <div class="name">Quillmere<small>PARTNERSHIP</small></div>
  </div>
  <h1 style="left:12px;top:60px;font-size:11px;line-height:1.15;font-weight:500" class="w"><b class="o" style="font-weight:800">Presentation Title</b><br>Goes Here</h1>
  <p style="left:12px;top:90px;font-size:5.4px;font-weight:800" class="o">Presentation Template</p>
  <p style="left:12px;top:97px;width:95px;font-size:3.3px;line-height:1.25" class="w">Lorem Ipsum is simply dummy text of the printing and typesetting industry.</p>
  <p style="left:12px;top:117px;font-size:3px;letter-spacing:.3px" class="w">Friday, July 18, 2025</p>
</section>

<section class="slide" style="left:280px;top:33px" aria-label="Business Marketing title">
  <div style="left:5px;top:5px;width:7px;height:7px;background:var(--orange)"></div>
  <div style="left:14px;top:33px">
    <div style="font-size:9.5px;font-weight:800;line-height:.9;color:var(--teal)">Quillmere<small style="display:block;font-size:3.3px;letter-spacing:.6px">PARTNERSHIP</small></div>
  </div>
  <h2 style="left:14px;top:63px;font-size:11.5px;line-height:1;font-weight:800"><span class="o">Business</span><br><span style="color:var(--teal)">Marketing</span></h2>
  <p style="left:14px;top:90px;font-size:6px;font-style:italic;font-weight:500">Presentation</p>
  <p class="t" style="left:14px;top:98px;width:70px;font-style:italic">Lorem ipsum dolor sit amet, consectetuer adipiscing elit, sed diam nonum</p>
  <div style="left:14px;top:117px;display:flex;gap:2px">
    <span style="width:2.5px;height:2.5px;border-radius:50%;background:var(--teal)"></span>
    <span style="width:2.5px;height:2.5px;border-radius:50%;background:var(--orange)"></span>
    <span style="width:2.5px;height:2.5px;border-radius:50%;background:var(--teal)"></span>
  </div>
  <div class="photo" role="img" aria-label="Photo of a presenter explaining charts to colleagues in an office" style="left:97px;top:0;width:134px;height:115px"></div>
  <div style="left:97px;top:115px;width:134px;height:15px;background:var(--teal);display:flex;align-items:center;justify-content:center;font-size:5px;letter-spacing:.3px" class="w">quillmerepartnership.co.uk</div>
</section>

<section class="slide" style="left:522px;top:33px" aria-label="Table of contents">
  <h2 style="left:10px;top:9px;font-size:8.5px;font-weight:500;line-height:1">Table of <b style="font-weight:800">Contents</b></h2>
  <div class="brand"><div class="mark"></div><div class="name">Quillmere<small>PARTNERSHIP</small></div></div>
  <div style="left:21px;top:37px;display:flex;flex-direction:column;gap:7.6px">
    <div class="toc-row">Simple Text One<span class="line"></span><span class="n">02</span></div>
    <div class="toc-row">Simple Text Two<span class="line"></span><span class="n">04</span></div>
    <div class="toc-row">Simple Text Three<span class="line"></span><span class="n">06</span></div>
    <div class="toc-row">Simple Text Four<span class="line"></span><span class="n">08</span></div>
    <div class="toc-row">Simple Text Five<span class="line"></span><span class="n">10</span></div>
  </div>
  <div style="left:121px;top:37px;display:flex;flex-direction:column;gap:7.6px">
    <div class="toc-row">Simple Text One<span class="line"></span><span class="n">02</span></div>
    <div class="toc-row">Simple Text Two<span class="line"></span><span class="n">04</span></div>
    <div class="toc-row">Simple Text Three<span class="line"></span><span class="n">06</span></div>
    <div class="toc-row">Simple Text Four<span class="line"></span><span class="n">08</span></div>
    <div class="toc-row">Simple Text Five<span class="line"></span><span class="n">10</span></div>
  </div>
  <div class="foot"><span>Copyright © 2025 Quillmere Partnership – All Rights Reserved.</span><span class="pg">2</span></div>
</section>

<!-- Row 2 -->
<section class="slide" style="left:35px;top:174px" aria-label="Values">
  <h2 class="heading"><b>Heading</b> Goes Here</h2>
  <div class="brand"><div class="mark"></div><div class="name">Quillmere<small>PARTNERSHIP</small></div></div>
  <div class="t" style="left:12px;top:31px;width:52px">
    <p>Lorem ipsum dolor sit amet, consectetuer adipiscing elit, sed diam nonummy nibh euismod tincidunt erat volutpat.</p>
    <p style="margin-top:2px">Ut wisi enim ad minim veniam, quis nostrud exerci tation ullamcorper suscipit lobortis nisl ut aliquip ex ea commodo consequat.</p>
    <p style="margin-top:2px">Lorem ipsum dolor sit amet, consectetuer adipiscing elit, nibh euismod tincidunt ut erat volutpat.</p>
    <p style="margin-top:2px">Ut wisi enim ad minim veniam, quis nostrud exerci tation ullamcorper suscipit lobortis nisl ut aliquip ex ea commodo consequat.</p>
  </div>
  <div class="photo" role="img" aria-label="Photos of smiling business people in a slanted frame" style="left:72px;top:25px;width:50px;height:86px;clip-path:polygon(40% 0,100% 0,60% 100%,0 100%)"></div>
  <div class="ring" style="left:120px;top:34px;width:12px;height:12px"><svg class="ic" width="7" height="7"><use href="#i-users"/></svg></div>
  <p class="h5" style="left:136px;top:36px"><span class="o">We</span> Before Me</p>
  <p class="t" style="left:136px;top:41px;width:70px">Ipsum dolor sit amet, cons ectetuer adipiscing elit, sed diam nonummy nibh euismod tincidunt ut laoreet</p>
  <div class="ring" style="left:108px;top:62px;width:12px;height:12px"><svg class="ic" width="7" height="7"><use href="#i-user"/></svg></div>
  <p class="h5" style="left:124px;top:63px"><span class="o">We Are</span> Good People</p>
  <p class="t" style="left:124px;top:68px;width:72px">Ipsum dolor sit amet, cons ectetuer adipiscing elit, sed diam nonummy nibh euismod tincidunt ut laoreet dolore magna aliquam erat volutpat.</p>
  <div class="ring" style="left:96px;top:90px;width:12px;height:12px"><svg class="ic" width="7" height="7"><use href="#i-heart"/></svg></div>
  <p class="h5" style="left:112px;top:91px"><span class="o">We Work</span> with Heart</p>
  <p class="t" style="left:112px;top:96px;width:72px">Ipsum dolor sit amet, cons ectetuer adipiscing elit, sed diam nonummy nibh euismod tincidunt</p>
  <div class="foot"><span>Copyright © 2025 Quillmere Partnership – All Rights Reserved.</span><span class="pg">3</span></div>
</section>

<section class="slide" style="left:280px;top:174px" aria-label="Idea promotion growth">
  <h2 class="heading"><b>Heading</b> Goes Here</h2>
  <div class="brand"><div class="mark"></div><div class="name">Quillmere<small>PARTNERSHIP</small></div></div>
  <div style="left:42px;top:30px;width:44px;height:58px;border:1.4px solid var(--teal);border-radius:4px;text-align:center;padding:4px 3px 0">
    <svg class="ic o" width="7" height="7" style="margin:0 auto 1px"><use href="#i-bulb"/></svg>
    <p class="h5" style="font-size:3.3px">IDEA</p><p class="t" style="font-size:2px">Lorem ipsum dolor sit amet, consectetuer adipiscing elit, sed diam nonummy nibh euismod tincidunt ut laoreet dolore magna aliquam erat volutpat.</p>
  </div>
  <div style="left:94px;top:30px;width:44px;height:58px;border:1.4px solid var(--teal);border-radius:4px;text-align:center;padding:4px 3px 0">
    <svg class="ic o" width="7" height="7" style="margin:0 auto 1px"><use href="#i-mail"/></svg>
    <p class="h5" style="font-size:3.3px">PROMOTION</p><p class="t" style="font-size:2px">Lorem ipsum dolor sit amet, consectetuer adipiscing elit, sed diam nonummy nibh euismod tincidunt ut laoreet dolore magna aliquam erat volutpat.</p>
  </div>
  <div style="left:146px;top:30px;width:44px;height:58px;border:1.4px solid var(--teal);border-radius:4px;text-align:center;padding:4px 3px 0">
    <svg class="ic o" width="7" height="7" style="margin:0 auto 1px"><use href="#i-growth"/></svg>
    <p class="h5" style="font-size:3.3px">GROWTH</p><p class="t" style="font-size:2px">Lorem ipsum dolor sit amet, consectetuer adipiscing elit, sed diam nonummy nibh euismod tincidunt ut laoreet dolore magna aliquam erat volutpat.</p>
  </div>
  <div style="left:85px;top:43px;width:4px;height:4px;border-radius:50%;background:var(--teal)"></div>
  <div style="left:137px;top:43px;width:4px;height:4px;border-radius:50%;background:var(--teal)"></div>
  <p class="t dk" style="left:28px;top:96px;width:175px;text-align:center">Lorem ipsum dolor sit amet, consectetuer adipiscing elit, sed diam nonummy nibh euismod tincidunt ut laoreet dolore magna aliquam erat volutpat. Ut wisi enim ad minim veniam, quis nostrud exerci tation ullamcorper suscipit lobortis nisl ut aliquip ex ea commodo consequat.</p>
  <div class="foot"><span>Copyright © 2025 Quillmere Partnership – All Rights Reserved.</span><span class="pg">4</span></div>
</section>

<section class="slide" style="left:522px;top:174px" aria-label="Mission and vision">
  <h2 class="heading"><b>Heading</b> Goes Here</h2>
  <div class="brand"><div class="mark"></div><div class="name">Quillmere<small>PARTNERSHIP</small></div></div>
  <p class="t dk" style="left:19px;top:32px;width:90px;font-size:3.1px;font-style:italic">Lorem ipsum dolor sit amet, cons ectetuer adipiscing elit, sed diam nonummy nibh euismod tincidunt. Lorem ipsum dolor sit amet.</p>
  <div class="photo round" role="img" aria-label="Photo of a team meeting in front of a whiteboard" style="left:19px;top:50px;width:87px;height:49px"></div>
  <div class="tile" style="left:119px;top:42px;width:17px;height:17px;display:flex;align-items:center;justify-content:center;color:var(--orange)"><svg class="ic" width="10" height="10"><use href="#i-flag"/></svg></div>
  <p class="h5" style="left:141px;top:42px;font-size:4.6px">Our <span class="o">Mission</span></p>
  <p class="t" style="left:141px;top:49px;width:66px;font-style:italic">Lorem ipsum dolor sit amet, cons ectetuer adipiscing elit, sed diam nonummy nibh euismod tincidunt.</p>
  <div class="tile" style="left:119px;top:74px;width:17px;height:17px;display:flex;align-items:center;justify-content:center;color:var(--orange)"><svg class="ic" width="10" height="10"><use href="#i-pen"/></svg></div>
  <p class="h5" style="left:141px;top:74px;font-size:4.6px">Our <span class="o">Vision</span></p>
  <p class="t" style="left:141px;top:81px;width:66px;font-style:italic">Lorem ipsum dolor sit amet, cons ectetuer adipiscing elit, sed diam nonummy nibh euismod tincidunt.</p>
  <div class="foot"><span>Copyright © 2025 Quillmere Partnership – All Rights Reserved.</span><span class="pg">5</span></div>
</section>

<!-- Row 3 -->
<section class="slide" style="left:35px;top:318px" aria-label="Problem and solution">
  <h2 class="heading"><b>Heading</b> Goes Here</h2>
  <div class="brand"><div class="mark"></div><div class="name">Quillmere<small>PARTNERSHIP</small></div></div>
  <div style="left:15px;top:42px;width:56px"><p class="h5"><span class="o">01.</span> Project Problem</p><p class="t">Lorem ipsum dolor sit amet, cons ectetuer adipiscing elit, sed diam nonummy nibh euismod tincidunt. Lorem ipsum dolor sit amet.</p></div>
  <div style="left:77px;top:42px;width:56px"><p class="h5"><span class="o">02.</span> Project Solution</p><p class="t">Lorem ipsum dolor sit amet, cons ectetuer adipiscing elit, sed diam nonummy nibh euismod tincidunt. Lorem ipsum dolor sit amet.</p></div>
  <div style="left:15px;top:74px;width:56px"><p class="h5"><span class="o">03.</span> Project Problem</p><p class="t">Lorem ipsum dolor sit amet, cons ectetuer adipiscing elit, sed diam nonummy nibh euismod tincidunt. Lorem ipsum dolor sit amet.</p></div>
  <div style="left:77px;top:74px;width:56px"><p class="h5"><span class="o">04.</span> Project Solution</p><p class="t">Lorem ipsum dolor sit amet, cons ectetuer adipiscing elit, sed diam nonummy nibh euismod tincidunt. Lorem ipsum dolor sit amet.</p></div>
  <div class="tile" style="left:136px;top:31px;width:37px;height:35px"><svg class="ic" width="6" height="6"><use href="#i-gear"/></svg><p class="h5">PROBLEM</p><p class="t">Lorem ipsum dolor sit amet, cons ectetuer adipiscing elit, sed diam nonummy.</p></div>
  <div class="tile" style="left:175px;top:31px;width:37px;height:35px"><svg class="ic" width="6" height="6"><use href="#i-bulb"/></svg><p class="h5">SOLUTION</p><p class="t">Lorem ipsum dolor sit amet, cons ectetuer adipiscing elit, sed diam nonummy.</p></div>
  <div class="tile" style="left:136px;top:68px;width:37px;height:35px"><svg class="ic" width="6" height="6"><use href="#i-chart"/></svg><p class="h5">MARKET</p><p class="t">Lorem ipsum dolor sit amet, cons ectetuer adipiscing elit, sed diam nonummy.</p></div>
  <div class="tile" style="left:175px;top:68px;width:37px;height:35px"><svg class="ic" width="6" height="6"><use href="#i-target"/></svg><p class="h5">MISSION</p><p class="t">Lorem ipsum dolor sit amet, cons ectetuer adipiscing elit, sed diam nonummy.</p></div>
  <div class="foot"><span>Copyright © 2025 Quillmere Partnership – All Rights Reserved.</span><span class="pg">6</span></div>
</section>

<section class="slide dark" style="left:280px;top:318px" aria-label="Section 01">
  <div class="dark-photo" role="img" aria-label="Dark teal photo of a desk with documents behind the section title"></div>
  <p class="part-no w" style="left:100px;top:50px">01</p>
  <p class="part-title" style="left:137px;top:53px">Part One.</p>
  <p style="left:137px;top:64px;width:68px;font-size:3.4px;line-height:1.25" class="w">Lorem ipsumectetuer adipiscing elit sed diam nonummy nibh euismod tincidunt</p>
  <div class="brand-big" style="right:9px;bottom:11px"><div class="name">Quillmere<small>PARTNERSHIP</small></div></div>
</section>

<section class="slide" style="left:522px;top:318px" aria-label="Text with photo">
  <h2 class="heading"><b>Heading</b> Goes Here</h2>
  <div class="brand"><div class="mark"></div><div class="name">Quillmere<small>PARTNERSHIP</small></div></div>
  <div style="left:16px;top:29px;width:114px"><p class="h5"><span class="o">01.</span> Text Added Here</p><p class="t" style="text-align:justify">Lorem ipsum dolor sit amet, cons ectetuer adipiscing elit, sed diam nonummy nibh euismod tincidunt ut laoreet dolore magna aliquam erat volutpat. Ut wisi enim ad minim veniam, quis nostrud exerci tation ullamcorper suscipit lobortis nisl ut aliquip ex ea commodo.</p></div>
  <div style="left:16px;top:56px;width:114px"><p class="h5"><span class="o">02.</span> Text Added Here</p><p class="t" style="text-align:justify">Lorem ipsum dolor sit amet, cons ectetuer adipiscing elit, sed diam nonummy nibh euismod tincidunt ut laoreet dolore magna aliquam erat volutpat. Ut wisi enim ad minim veniam, quis nostrud exerci tation ullamcorper suscipit lobortis nisl ut aliquip ex ea commodo.</p></div>
  <div style="left:16px;top:86px;width:114px"><p class="h5"><span class="o">03.</span> Text Added Here</p><p class="t" style="text-align:justify">Lorem ipsum dolor sit amet, cons ectetuer adipiscing elit, sed diam nonummy nibh euismod tincidunt ut laoreet dolore magna aliquam erat volutpat. Ut wisi enim ad minim veniam, quis nostrud exerci tation ullamcorper suscipit lobortis nisl ut aliquip ex ea commodo.</p></div>
  <div class="photo warm" role="img" aria-label="Photo of two businessmen reviewing a tablet" style="left:136px;top:32px;width:72px;height:77px"></div>
  <div class="foot"><span>Copyright © 2025 Quillmere Partnership – All Rights Reserved.</span><span class="pg">8</span></div>
</section>

<!-- Row 4 -->
<section class="slide" style="left:35px;top:460px" aria-label="Bar chart">
  <h2 class="heading"><b>Heading</b> Goes Here</h2>
  <div class="brand"><div class="mark"></div><div class="name">Quillmere<small>PARTNERSHIP</small></div></div>
  <svg style="left:14px;top:33px" width="100" height="78" viewBox="0 0 100 78">
    <g font-size="2" fill="#8d9597" font-family="Red Hat Display, sans-serif">
      <text x="2" y="65">0</text><text x="2" y="54">1</text><text x="2" y="43">2</text><text x="2" y="32">3</text><text x="2" y="21">4</text><text x="2" y="10">5</text>
      <text x="14" y="71">Category 1</text><text x="43" y="71">Category 1</text><text x="72" y="71">Category 1</text>
      <text x="30" y="76">■ Series 1 ■ Series 1 ■ Series 1</text>
    </g>
    <line x1="7" y1="64" x2="96" y2="64" stroke="#c7cbcd" stroke-width=".4"/>
    <rect x="13" y="14" width="4" height="50" fill="#163a3f"/><rect x="18" y="24" width="4" height="40" fill="#e8561c"/><rect x="23" y="33" width="4" height="31" fill="#c7cbcd"/>
    <rect x="42" y="14" width="4" height="50" fill="#163a3f"/><rect x="47" y="5" width="4" height="59" fill="#e8561c"/><rect x="52" y="17" width="4" height="47" fill="#c7cbcd"/>
    <rect x="71" y="12" width="4" height="52" fill="#163a3f"/><rect x="76" y="33" width="4" height="31" fill="#e8561c"/><rect x="81" y="17" width="4" height="47" fill="#c7cbcd"/>
  </svg>
  <div class="num" style="left:122px;top:40px;background:var(--teal)">1</div>
  <div style="left:136px;top:37px;width:72px"><p class="h5" style="font-size:4.4px">Lorem ipsum dolor.</p><p class="t">Lorem ipsumectetuer adipiscing elit, sed diam nonummy nibh euismod tincidunt sed diam nonummy nihhunt</p></div>
  <div class="num" style="left:122px;top:67px;background:var(--orange)">2</div>
  <div style="left:136px;top:64px;width:72px"><p class="h5 o" style="font-size:4.4px">Lorem ipsum dolor.</p><p class="t">Lorem ipsumectetuer adipiscing elit, sed diam nonummy nibh euismod tincidunt sed diam nonummy nihhunt</p></div>
  <div class="num" style="left:122px;top:94px;background:var(--gray)">3</div>
  <div style="left:136px;top:91px;width:72px"><p class="h5" style="font-size:4.4px;color:var(--mute)">Lorem ipsum dolor.</p><p class="t">Lorem ipsumectetuer adipiscing elit, sed diam nonummy nibh euismod tincidunt sed diam nonummy nihhunt</p></div>
  <div class="foot"><span>Copyright © 2025 Quillmere Partnership – All Rights Reserved.</span><span class="pg">9</span></div>
</section>

<section class="slide" style="left:280px;top:460px" aria-label="Market analysis pie chart">
  <h2 class="heading"><b>Heading</b> Goes Here</h2>
  <div class="brand"><div class="mark"></div><div class="name">Quillmere<small>PARTNERSHIP</small></div></div>
  <p style="left:15px;top:28px;font-size:6px;line-height:1.1;font-weight:500">Market Analysis<br><b style="font-weight:800">For A <span class="o">Business Plan</span></b></p>
  <div style="left:15px;top:51px;width:70px"><p class="h5"><span class="o">01.</span> Lorem ipsum dolor.</p><p class="t">Lorem ipsumectetuer adipiscing elit, sed diam nonummy nibh euismod tincidunt</p></div>
  <div style="left:15px;top:72px;width:70px"><p class="h5"><span class="o">02.</span> Lorem ipsum dolor.</p><p class="t">Lorem ipsumectetuer adipiscing elit, sed diam nonummy nibh euismod tincidunt</p></div>
  <div style="left:15px;top:90px;width:70px"><p class="h5"><span class="o">03.</span> Lorem ipsum dolor.</p><p class="t">Lorem ipsumectetuer adipiscing elit, sed diam nonummy nibh euismod tincidunt</p></div>
  <svg style="left:104px;top:26px" width="100" height="70" viewBox="0 0 100 70">
    <g transform="translate(50 35) scale(1 .85) translate(-50 -35)">
      <path d="M53,35 L53,5 A30,30 0 0 1 53,65 Z" fill="#163a3f"/>
      <path d="M50,35 L50,65 A30,30 0 0 1 21.5,25.7 Z" fill="#e8561c"/>
      <path d="M50,35 L21.5,25.7 A30,30 0 0 1 50,5 Z" fill="#c7cbcd"/>
    </g>
  </svg>
  <p style="left:112px;top:100px;font-size:4.3px;display:flex;gap:8px"><span><b style="color:var(--teal)">■</b> Series 1</span><span><b class="o">■</b> Series 1</span><span><b style="color:var(--gray)">■</b> Series 1</span></p>
  <div class="foot"><span>Copyright © 2025 Quillmere Partnership – All Rights Reserved.</span><span class="pg">10</span></div>
</section>

<section class="slide" style="left:522px;top:460px" aria-label="Cycle diagram">
  <h2 class="heading"><b>Heading</b> Goes Here</h2>
  <div class="brand"><div class="mark"></div><div class="name">Quillmere<small>PARTNERSHIP</small></div></div>
  <div class="t" style="left:14px;top:30px;width:68px">
    <p>Lorem ipsum dolor sit amet, consectetuer adipiscing elit, sed diam nonummy nibh.</p>
    <p style="margin-top:2px">Ut wisi enim ad minim veniam, quis nostrud exerci tation ullamcorper suscipit lobortis. Ut wisi enim ad minim veniam, quis nostrud exerci tation ullamcorper suscipit lobortis.</p>
  </div>
  <p class="h5 o" style="left:20px;top:75px;font-size:3.3px">● <span style="color:var(--ink)">Lorem ipsum</span></p>
  <p class="t" style="left:23px;top:79px;width:58px">Lorem ipsum dolor sit amet, consectetuer adipiscing elit, sed diam nonummy.</p>
  <p class="h5 o" style="left:20px;top:90px;font-size:3.3px">● <span style="color:var(--ink)">Lorem ipsum</span></p>
  <p class="t" style="left:23px;top:94px;width:58px">Lorem ipsum dolor sit amet, consectetuer adipiscing elit, sed diam nonummy.</p>
  <svg style="left:95px;top:25px" width="136" height="95" viewBox="0 0 136 95">
    <path d="M55,47 A30,30 0 1 1 85,77" fill="none" stroke="#163a3f" stroke-width="2.4"/>
    <path d="M50,40 l5,8 l5,-8" fill="none" stroke="#163a3f" stroke-width="2"/>
    <circle cx="80" cy="25" r="9" fill="#fff" stroke="#163a3f" stroke-width="2.6"/>
    <circle cx="79" cy="24" r="3" fill="none" stroke="#e8561c" stroke-width="1"/><line x1="81" y1="26" x2="83.5" y2="28.5" stroke="#e8561c" stroke-width="1"/>
    <circle cx="81" cy="55" r="8" fill="#fff" stroke="#e8561c" stroke-width="2.6"/>
    <path d="M81,51 a3,3 0 0 1 1.5,5.6 v1.4 h-3 v-1.4 A3,3 0 0 1 81,51z" fill="#163a3f"/>
    <circle cx="71" cy="78" r="6" fill="#fff" stroke="#163a3f" stroke-width="2"/>
    <path d="M71,75 v6 M68.5,78.5 a2.5,2.5 0 0 0 5,0" fill="none" stroke="#e8561c" stroke-width=".8"/>
    <circle cx="41" cy="70" r="5" fill="#fff" stroke="#e8561c" stroke-width="2"/>
    <circle cx="41" cy="70" r="2" fill="none" stroke="#163a3f" stroke-width=".8"/>
    <rect x="46" y="27" width="2" height="5" fill="#e8561c"/><rect x="49" y="24" width="2" height="8" fill="#163a3f"/><rect x="52" y="29" width="2" height="3" fill="#e8561c"/>
    <g font-family="Red Hat Display, sans-serif" font-weight="700" font-size="2.8" fill="#243033">
      <text x="40" y="37">MAIN TITLE</text>
      <text x="104" y="17">Your Title</text><text x="108" y="51">Your Title</text>
      <text x="15" y="66">Your Title</text><text x="104" y="82">Your Title</text>
    </g>
    <g font-family="Red Hat Display, sans-serif" font-size="1.7" fill="#8d9597">
      <text x="104" y="20">Lorem ipsum dolor sit</text><text x="108" y="54">Lorem ipsum dolor sit</text>
      <text x="15" y="69">Lorem ipsum dolor sit</text><text x="104" y="85">Lorem ipsum dolor sit</text>
      <text x="40" y="40">Lorem ipsum dolor</text>
    </g>
    <g font-family="Red Hat Display, sans-serif" font-weight="700" font-size="2.2" fill="#e8561c">
      <text x="96" y="11">65%</text><text x="64" y="48">40%</text><text x="49" y="65">50%</text><text x="84" y="91">75%</text>
    </g>
  </svg>
  <div class="foot"><span>Copyright © 2025 Quillmere Partnership – All Rights Reserved.</span><span class="pg">11</span></div>
</section>

<!-- Row 5 -->
<section class="slide" style="left:35px;top:605px" aria-label="Three options">
  <h2 class="heading"><b>Heading</b> Goes Here</h2>
  <div class="brand"><div class="mark"></div><div class="name">Quillmere<small>PARTNERSHIP</small></div></div>
  <svg style="left:10px;top:52px" width="26" height="26" viewBox="0 0 26 26"><path d="M2,0 L13,0 L25,13 L13,26 L2,26 L14,13 Z" fill="#e2e5e6"/></svg>
  <div class="photo" role="img" aria-label="Photo of colleagues working at laptops" style="left:51px;top:28px;width:42px;height:50px;border-bottom:1.5px solid var(--orange)"></div>
  <div class="photo warm" role="img" aria-label="Photo of a business meeting around a table" style="left:105px;top:28px;width:42px;height:50px;border-bottom:1.5px solid var(--orange)"></div>
  <div class="photo" role="img" aria-label="Photo of business partners shaking hands" style="left:160px;top:28px;width:42px;height:50px;border-bottom:1.5px solid var(--orange)"></div>
  <div style="left:51px;top:81px;width:42px"><p class="h5"><span class="o">First</span> Option</p><p class="t">Lorem ipsum dolor sit consectetuer adipiscing elit, sed diam nonummy nibh euismod tincidunt ut dolore magna aliquam erat volutpat.</p></div>
  <div style="left:105px;top:81px;width:42px"><p class="h5"><span class="o">Second</span> Option</p><p class="t">Lorem ipsum dolor sit consectetuer adipiscing elit, sed diam nonummy nibh euismod tincidunt ut dolore magna aliquam erat volutpat.</p></div>
  <div style="left:160px;top:81px;width:42px"><p class="h5"><span class="o">Third</span> Option</p><p class="t">Lorem ipsum dolor sit consectetuer adipiscing elit, sed diam nonummy nibh euismod tincidunt ut dolore magna aliquam erat volutpat.</p></div>
  <div class="foot"><span>Copyright © 2025 Quillmere Partnership – All Rights Reserved.</span><span class="pg">12</span></div>
</section>

<section class="slide" style="left:280px;top:605px" aria-label="Four part circle">
  <h2 class="heading"><b>Heading</b> Goes Here</h2>
  <div class="brand"><div class="mark"></div><div class="name">Quillmere<small>PARTNERSHIP</small></div></div>
  <svg style="left:80px;top:30px" width="72" height="72" viewBox="80 30 72 72">
    <g stroke="#fff" stroke-width="1.2">
      <path d="M116,35 A31,31 0 0 1 147,66 L130,66 A14,14 0 0 0 116,52 Z" fill="#e8561c"/>
      <path d="M147,66 A31,31 0 0 1 116,97 L116,80 A14,14 0 0 0 130,66 Z" fill="#163a3f"/>
      <path d="M116,97 A31,31 0 0 1 85,66 L102,66 A14,14 0 0 0 116,80 Z" fill="#e8561c"/>
      <path d="M85,66 A31,31 0 0 1 116,35 L116,52 A14,14 0 0 0 102,66 Z" fill="#163a3f"/>
    </g>
    <use href="#i-target" x="96" y="41" width="9" height="9" style="fill:none;stroke:#fff;stroke-width:1.8"/>
    <use href="#i-rocket" x="127" y="41" width="9" height="9" style="fill:none;stroke:#fff;stroke-width:1.8"/>
    <use href="#i-coin" x="96" y="78" width="9" height="9" style="fill:none;stroke:#fff;stroke-width:1.8"/>
    <use href="#i-gear" x="127" y="78" width="9" height="9" style="fill:none;stroke:#fff;stroke-width:1.8"/>
    <text x="116" y="65" text-anchor="middle" font-family="Red Hat Display, sans-serif" font-weight="800" font-size="4.6" fill="#243033">Text</text>
    <text x="116" y="70.5" text-anchor="middle" font-family="Red Hat Display, sans-serif" font-weight="800" font-size="4.6" fill="#243033">Added</text>
  </svg>
  <div style="left:25px;top:33px;width:52px;text-align:right"><p class="h5 o">Text Here</p><p class="t">Lorem ipsum dolor sit amet, consectetuer adipiscing elit, sed diammy nibh euismod tincidunt ut laoreet dolore</p></div>
  <div style="left:155px;top:33px;width:52px"><p class="h5">Text Here</p><p class="t">Lorem ipsum dolor sit amet, consectetuer adipiscing elit, sed diammy nibh euismod tincidunt ut laoreet dolore</p></div>
  <div style="left:25px;top:80px;width:52px;text-align:right"><p class="h5">Text Here</p><p class="t">Lorem ipsum dolor sit amet, consectetuer adipiscing elit, sed diammy nibh euismod tincidunt ut laoreet dolore</p></div>
  <div style="left:155px;top:80px;width:52px"><p class="h5 o">Text Here</p><p class="t">Lorem ipsum dolor sit amet, consectetuer adipiscing elit, sed diammy nibh euismod tincidunt ut laoreet dolore</p></div>
  <div class="foot"><span>Copyright © 2025 Quillmere Partnership – All Rights Reserved.</span><span class="pg">13</span></div>
</section>

<section class="slide" style="left:522px;top:605px" aria-label="Six text blocks">
  <h2 class="heading"><b>Heading</b> Goes Here</h2>
  <div class="brand"><div class="mark"></div><div class="name">Quillmere<small>PARTNERSHIP</small></div></div>
  <div style="left:14px;top:31px;width:62px"><p class="h5"><span class="o">01.</span> Text Added Here</p><p class="t">Lorem ipsum dolor sit amet, cons ectetuer adipiscing elit, sed diam nonummy nibh euismod tincidunt ut laoreet dolore magna aliquam erat volutpat. Ut wisi enim ad minim veniam.</p></div>
  <div style="left:83px;top:31px;width:62px"><p class="h5">02. <span class="o">Text Added Here</span></p><p class="t">Lorem ipsum dolor sit amet, cons ectetuer adipiscing elit, sed diam nonummy nibh euismod tincidunt ut laoreet dolore magna aliquam erat volutpat. Ut wisi enim ad minim veniam.</p></div>
  <div style="left:151px;top:31px;width:62px"><p class="h5"><span class="o">03.</span> Text Added Here</p><p class="t">Lorem ipsum dolor sit amet, cons ectetuer adipiscing elit, sed diam nonummy nibh euismod tincidunt ut laoreet dolore magna aliquam erat volutpat. Ut wisi enim ad minim veniam.</p></div>
  <div style="left:14px;top:73px;width:62px"><p class="h5">04. <span class="o">Text Added Here</span></p><p class="t">Lorem ipsum dolor sit amet, cons ectetuer adipiscing elit, sed diam nonummy nibh euismod tincidunt ut laoreet dolore magna aliquam erat volutpat. Ut wisi enim ad minim veniam.</p></div>
  <div style="left:83px;top:73px;width:62px"><p class="h5"><span class="o">05.</span> Text Added Here</p><p class="t">Lorem ipsum dolor sit amet, cons ectetuer adipiscing elit, sed diam nonummy nibh euismod tincidunt ut laoreet dolore magna aliquam erat volutpat. Ut wisi enim ad minim veniam.</p></div>
  <div style="left:151px;top:73px;width:62px"><p class="h5">06. <span class="o">Text Added Here</span></p><p class="t">Lorem ipsum dolor sit amet, cons ectetuer adipiscing elit, sed diam nonummy nibh euismod tincidunt ut laoreet dolore magna aliquam erat volutpat. Ut wisi enim ad minim veniam.</p></div>
  <div class="foot"><span>Copyright © 2025 Quillmere Partnership – All Rights Reserved.</span><span class="pg">14</span></div>
</section>

<!-- Row 6 -->
<section class="slide dark" style="left:35px;top:750px" aria-label="Section 02">
  <div class="dark-photo" role="img" aria-label="Dark teal photo of a desk with documents behind the section title"></div>
  <p class="part-no o" style="left:93px;top:60px">02</p>
  <p class="part-title" style="left:134px;top:64px">Part One.</p>
  <p style="left:134px;top:75px;width:70px;font-size:3.4px;line-height:1.25" class="w">Lorem ipsumectetuer adipiscing elit sed diam nonummy nibh euismod tincidunt</p>
  <div class="brand-big" style="right:9px;bottom:11px"><div class="name">Quillmere<small>PARTNERSHIP</small></div></div>
</section>

<section class="slide" style="left:280px;top:750px" aria-label="Six icon features">
  <h2 class="heading"><b>Heading</b> Goes Here</h2>
  <div class="brand"><div class="mark"></div><div class="name">Quillmere<small>PARTNERSHIP</small></div></div>
  <div style="left:28px;top:27px;width:48px;text-align:center"><div class="feature-box line"><svg class="ic" width="11" height="11"><use href="#i-users"/></svg></div><p class="h5" style="font-size:3.3px">LOREM IPSUM</p><p class="t" style="font-size:2.2px">Lorem ipsum dolor sit amet, consectetuer adipiscing elit, sed diam nonummy nibh euismod tincidunt ut laoreet</p></div>
  <div style="left:92px;top:27px;width:48px;text-align:center"><div class="feature-box fill"><svg class="ic" width="11" height="11"><use href="#i-gear"/></svg></div><p class="h5 o" style="font-size:3.3px">LOREM IPSUM</p><p class="t" style="font-size:2.2px">Lorem ipsum dolor sit amet, consectetuer adipiscing elit, sed diam nonummy nibh euismod tincidunt ut laoreet</p></div>
  <div style="left:156px;top:27px;width:48px;text-align:center"><div class="feature-box line"><svg class="ic" width="11" height="11"><use href="#i-growth"/></svg></div><p class="h5" style="font-size:3.3px">LOREM IPSUM</p><p class="t" style="font-size:2.2px">Lorem ipsum dolor sit amet, consectetuer adipiscing elit, sed diam nonummy nibh euismod tincidunt ut laoreet</p></div>
  <div style="left:28px;top:72px;width:48px;text-align:center"><div class="feature-box fill"><svg class="ic" width="11" height="11"><use href="#i-down"/></svg></div><p class="h5 o" style="font-size:3.3px">LOREM IPSUM</p><p class="t" style="font-size:2.2px">Lorem ipsum dolor sit amet, consectetuer adipiscing elit, sed diam nonummy nibh euismod tincidunt ut laoreet</p></div>
  <div style="left:92px;top:72px;width:48px;text-align:center"><div class="feature-box line"><svg class="ic" width="11" height="11"><use href="#i-coin"/></svg></div><p class="h5" style="font-size:3.3px">LOREM IPSUM</p><p class="t" style="font-size:2.2px">Lorem ipsum dolor sit amet, consectetuer adipiscing elit, sed diam nonummy nibh euismod tincidunt ut laoreet</p></div>
  <div style="left:156px;top:72px;width:48px;text-align:center"><div class="feature-box fill"><svg class="ic" width="11" height="11"><use href="#i-award"/></svg></div><p class="h5 o" style="font-size:3.3px">LOREM IPSUM</p><p class="t" style="font-size:2.2px">Lorem ipsum dolor sit amet, consectetuer adipiscing elit, sed diam nonummy nibh euismod tincidunt ut laoreet</p></div>
  <div class="foot"><span>Copyright © 2025 Quillmere Partnership – All Rights Reserved.</span><span class="pg">15</span></div>
</section>

<section class="slide" style="left:522px;top:750px" aria-label="Two columns of text">
  <h2 class="heading"><b>Heading</b> Goes Here</h2>
  <div class="brand"><div class="mark"></div><div class="name">Quillmere<small>PARTNERSHIP</small></div></div>
  <div style="left:18px;top:30px;width:93px">
    <p class="h5" style="font-size:6px">01. <span class="o">Text Added Here</span></p>
    <p class="t" style="text-align:justify;margin-top:2px">Lorem ipsum dolor sit amet, cons ectetuer adipiscing elit, sed diam nonummy nibh euismod tincidunt ut laoreet dolore magna aliquam erat volutpat. Ut wisi enim ad minim veniam, quis nostrud exerci tation ullamcorper suscipit lobortis nisl ut aliquip ex ea commodo consequat.</p>
    <p class="t" style="text-align:justify;margin-top:2px">Lorem ipsum dolor sit amet, consectetuer adipiscing elit, sed diam nonummy nibh euismod tincidunt ut laoreet dolore magna aliquam erat volutpat. Ut wisi enim ad minim veniam, quis nostrud exerci tation ullamcorper.</p>
    <p class="t" style="text-align:justify;margin-top:2px">Lorem ipsum dolor sit amet, consectetuer adipiscing elit, sed diam nonummy nibh euismod tincidunt ut laoreet dolore magna aliquam erat volutpat.</p>
  </div>
  <div style="left:118px;top:30px;width:93px">
    <p class="h5" style="font-size:6px">02. <span class="o">Text Added Here</span></p>
    <p class="t" style="text-align:justify;margin-top:2px">Lorem ipsum dolor sit amet, cons ectetuer adipiscing elit, sed diam nonummy nibh euismod tincidunt ut laoreet dolore magna aliquam erat volutpat. Ut wisi enim ad minim veniam, quis nostrud exerci tation ullamcorper suscipit lobortis nisl ut aliquip ex ea commodo consequat.</p>
    <p class="t" style="text-align:justify;margin-top:2px">Lorem ipsum dolor sit amet, consectetuer adipiscing elit, sed diam nonummy nibh euismod tincidunt ut laoreet dolore magna aliquam erat volutpat. Ut wisi enim ad minim veniam, quis nostrud exerci tation ullamcorper.</p>
    <p class="t" style="text-align:justify;margin-top:2px">Lorem ipsum dolor sit amet, consectetuer adipiscing elit, sed diam nonummy nibh euismod tincidunt ut laoreet dolore magna aliquam erat volutpat.</p>
  </div>
  <div class="foot"><span>Copyright © 2025 Quillmere Partnership – All Rights Reserved.</span><span class="pg">16</span></div>
</section>

<!-- Row 7 -->
<section class="slide" style="left:35px;top:894px" aria-label="Timeline">
  <h2 class="heading"><b>Heading</b> Goes Here</h2>
  <div class="brand"><div class="mark"></div><div class="name">Quillmere<small>PARTNERSHIP</small></div></div>
  <svg style="left:0;top:0" width="231" height="130" viewBox="0 0 231 130">
    <polygon points="22,68 28,62 60,62 57,68" fill="#163a3f"/>
    <polygon points="59,68 62,62 97,62 94,68" fill="#e8561c"/>
    <polygon points="96,68 99,62 134,62 131,68" fill="#163a3f"/>
    <polygon points="133,68 136,62 171,62 168,68" fill="#e8561c"/>
    <polygon points="170,68 173,62 205,62 211,68" fill="#163a3f"/>
    <g font-family="Red Hat Display, sans-serif" font-weight="700" font-size="3.3" fill="#fff" text-anchor="middle">
      <text x="41" y="66.3">1990</text><text x="78" y="66.3">2001</text><text x="115" y="66.3">2007</text><text x="152" y="66.3">2012</text><text x="190" y="66.3">2020</text>
    </g>
    <g stroke-width=".8">
      <line x1="41" y1="49" x2="41" y2="60" stroke="#e8561c"/><circle cx="41" cy="49" r="1.2" fill="#e8561c"/>
      <line x1="115" y1="49" x2="115" y2="60" stroke="#e8561c"/><circle cx="115" cy="49" r="1.2" fill="#e8561c"/>
      <line x1="190" y1="49" x2="190" y2="60" stroke="#e8561c"/><circle cx="190" cy="49" r="1.2" fill="#e8561c"/>
      <line x1="78" y1="70" x2="78" y2="80" stroke="#163a3f"/><circle cx="78" cy="80" r="1.2" fill="#163a3f"/>
      <line x1="152" y1="70" x2="152" y2="80" stroke="#163a3f"/><circle cx="152" cy="80" r="1.2" fill="#163a3f"/>
    </g>
    <g font-family="Red Hat Display, sans-serif" text-anchor="middle">
      <text x="41" y="38" font-size="3.6" font-weight="700" fill="#e8561c">YOUR TITLE</text>
      <text x="41" y="42" font-size="2.6" fill="#8d9597">Refers to a good or</text><text x="41" y="45.3" font-size="2.6" fill="#8d9597">service being offered</text>
      <text x="115" y="38" font-size="3.6" font-weight="700" fill="#e8561c">YOUR TITLE</text>
      <text x="115" y="42" font-size="2.6" fill="#8d9597">Refers to a good or</text><text x="115" y="45.3" font-size="2.6" fill="#8d9597">service being offered</text>
      <text x="190" y="38" font-size="3.6" font-weight="700" fill="#e8561c">YOUR TITLE</text>
      <text x="190" y="42" font-size="2.6" fill="#8d9597">Refers to a good or</text><text x="190" y="45.3" font-size="2.6" fill="#8d9597">service being offered</text>
      <text x="78" y="88" font-size="3.6" font-weight="700" fill="#163a3f">YOUR TITLE</text>
      <text x="78" y="92" font-size="2.6" fill="#8d9597">Refers to a good or</text><text x="78" y="95.3" font-size="2.6" fill="#8d9597">service being offered</text>
      <text x="152" y="88" font-size="3.6" font-weight="700" fill="#163a3f">YOUR TITLE</text>
      <text x="152" y="92" font-size="2.6" fill="#8d9597">Refers to a good or</text><text x="152" y="95.3" font-size="2.6" fill="#8d9597">service being offered</text>
    </g>
  </svg>
  <div class="foot"><span>Copyright © 2025 Quillmere Partnership – All Rights Reserved.</span><span class="pg">17</span></div>
</section>

<section class="slide" style="left:280px;top:894px" aria-label="Text with bullet list">
  <h2 class="heading"><b>Heading</b> Goes Here</h2>
  <div class="brand"><div class="mark"></div><div class="name">Quillmere<small>PARTNERSHIP</small></div></div>
  <div style="left:19px;top:29px;width:90px">
    <p class="h5"><span class="o">01.</span> Text Added Here</p>
    <p class="t" style="text-align:justify">Lorem ipsum dolor sit amet, cons ectetuer adipiscing elit, sed diam nonummy nibh euismod tincidunt ut laoreet dolore magna aliquam erat volutpat. Ut wisi enim ad minim veniam, quis nostrud exerci tation ullamcorper suscipit lobortis nisl ut aliquip ex ea commodo consequat.</p>
    <p class="t" style="text-align:justify;margin-top:2px">Lorem ipsum dolor sit amet, consectetuer adipiscing elit, sed diam nonummy nibh euismod tincidunt ut laoreet dolore magna aliquam erat volutpat. Ut wisi enim ad minim veniam, quis nostrud exerci tation.</p>
    <p class="h5" style="margin-top:3px"><span class="o">02.</span> Text Added Here</p>
    <p class="t" style="text-align:justify">Lorem ipsum dolor sit amet, cons ectetuer adipiscing elit, sed diam nonummy nibh euismod tincidunt ut laoreet dolore magna aliquam erat volutpat. Ut wisi enim ad minim veniam, quis nostrud exerci tation ullamcorper suscipit lobortis nisl ut aliquip ex ea commodo consequat.</p>
    <p class="t" style="text-align:justify;margin-top:2px">Lorem ipsum dolor sit amet, consectetuer adipiscing elit, sed diam nonummy nibh euismod tincidunt ut laoreet dolore magna aliquam.</p>
  </div>
  <div style="left:125px;top:35px;display:flex;flex-direction:column;gap:7.6px">
    <p class="bullet">Fits Your Business Or Products</p>
    <p class="bullet">Is Easy To Spell And Remember</p>
    <p class="bullet">Fits Your Business Or Products</p>
    <p class="bullet">Is Easy To Spell And Remember</p>
    <p class="bullet">Fits Your Business Or Products</p>
    <p class="bullet">Is Easy To Spell And Remember</p>
  </div>
  <div class="foot"><span>Copyright © 2025 Quillmere Partnership – All Rights Reserved.</span><span class="pg">18</span></div>
</section>

<section class="slide" style="left:522px;top:894px" aria-label="Four steps">
  <h2 class="heading"><b>Heading</b> Goes Here</h2>
  <div class="brand"><div class="mark"></div><div class="name">Quillmere<small>PARTNERSHIP</small></div></div>
  <svg style="left:0;top:0" width="231" height="130" viewBox="0 0 231 130">
    <rect x="17" y="56" width="92" height="3" fill="#163a3f"/>
    <rect x="109" y="56" width="94" height="3" fill="#e8561c"/>
    <polygon points="203,53.5 210,57.5 203,61.5" fill="#e8561c"/>
    <g fill="#fff" stroke-width="2.8">
      <circle cx="56" cy="46" r="9" stroke="#163a3f"/>
      <circle cx="96" cy="46" r="9" stroke="#e8561c"/>
      <circle cx="136" cy="46" r="9" stroke="#163a3f"/>
      <circle cx="176" cy="46" r="9" stroke="#e8561c"/>
    </g>
    <use href="#i-clock" x="51.5" y="41.5" width="9" height="9" style="fill:none;stroke:#e8561c;stroke-width:1.8"/>
    <circle cx="96" cy="46" r="4.5" fill="#163a3f"/>
    <use href="#i-coin" x="92.5" y="42.5" width="7" height="7" style="fill:none;stroke:#fff;stroke-width:2"/>
    <use href="#i-db" x="131.5" y="41.5" width="9" height="9" style="fill:none;stroke:#e8561c;stroke-width:1.8"/>
    <use href="#i-search" x="171.5" y="41.5" width="9" height="9" style="fill:none;stroke:#163a3f;stroke-width:1.8"/>
    <g font-family="Red Hat Display, sans-serif" font-weight="700" font-size="2.6" fill="#fff" text-anchor="middle">
      <text x="73" y="58.4">Step 01</text><text x="113" y="58.4">Step 02</text><text x="153" y="58.4">Step 03</text><text x="193" y="58.4">Step 04</text>
    </g>
    <g stroke="#163a3f" stroke-width=".7"><line x1="56" y1="61" x2="56" y2="67"/><line x1="96" y1="61" x2="96" y2="67"/><line x1="136" y1="61" x2="136" y2="67"/><line x1="176" y1="61" x2="176" y2="67"/></g>
  </svg>
  <div style="left:41px;top:70px;width:30px;text-align:center"><p class="h5">Lorem Ipsum</p><p class="t" style="font-size:2.1px">Lorem ipsum dolor sit amet, consectetuer adipiscing elit sed diam nonummy nibh euismod tincidunt ut laoreet dolore magna aliquam erat volutpat.</p></div>
  <div style="left:81px;top:70px;width:30px;text-align:center"><p class="h5">Lorem Ipsum</p><p class="t" style="font-size:2.1px">Lorem ipsum dolor sit amet, consectetuer adipiscing elit sed diam nonummy nibh euismod tincidunt ut laoreet dolore magna aliquam erat volutpat.</p></div>
  <div style="left:121px;top:70px;width:30px;text-align:center"><p class="h5">Lorem Ipsum</p><p class="t" style="font-size:2.1px">Lorem ipsum dolor sit amet, consectetuer adipiscing elit sed diam nonummy nibh euismod tincidunt ut laoreet dolore magna aliquam erat volutpat.</p></div>
  <div style="left:161px;top:70px;width:30px;text-align:center"><p class="h5">Lorem Ipsum</p><p class="t" style="font-size:2.1px">Lorem ipsum dolor sit amet, consectetuer adipiscing elit sed diam nonummy nibh euismod tincidunt ut laoreet dolore magna aliquam erat volutpat.</p></div>
  <div class="foot"><span>Copyright © 2025 Quillmere Partnership – All Rights Reserved.</span><span class="pg">19</span></div>
</section>

<!-- Row 8 -->
<section class="slide" style="left:35px;top:1037px" aria-label="Mobile screens">
  <h2 class="heading"><b>Heading</b> Goes Here</h2>
  <div class="brand"><div class="mark"></div><div class="name">Quillmere<small>PARTNERSHIP</small></div></div>
  <div class="t dk" style="left:16px;top:30px;width:72px">
    <p>Lorem ipsum dolor sit amet, consectetuer adipiscing elit, sed diam nonummy nibh euismod tincidunt ut laoreet dolore magna aliquam erat volutpat. Ut wisi enim ad minim veniam,</p>
    <p style="margin-top:2px">quis nostrud exerci tation ullamcorper suscipit lobortis nisl ut aliquip ex ea commodo consequat. Duis autem vel eum iriure dolor in hendrerit in vulputate velit esse</p>
  </div>
  <div style="left:23px;top:67px;display:flex;flex-direction:column;gap:5px;width:70px">
    <div style="display:flex;gap:3px"><div class="num" style="flex:none;width:6px;height:6px;border-radius:0;background:var(--teal);font-size:3.5px">1.</div><div><p class="h5 o" style="font-size:3.3px">Lorem ipsum</p><p class="t" style="font-size:2px">Lorem ipsum dolor sit amet, consectetuer adipiscing elit, sed diam nonummy nibh euismod tincidunt</p></div></div>
    <div style="display:flex;gap:3px"><div class="num" style="flex:none;width:6px;height:6px;border-radius:0;background:var(--teal);font-size:3.5px">2.</div><div><p class="h5 o" style="font-size:3.3px">Lorem ipsum</p><p class="t" style="font-size:2px">Lorem ipsum dolor sit amet, consectetuer adipiscing elit, sed diam nonummy nibh euismod tincidunt</p></div></div>
    <div style="display:flex;gap:3px"><div class="num" style="flex:none;width:6px;height:6px;border-radius:0;background:var(--teal);font-size:3.5px">3.</div><div><p class="h5 o" style="font-size:3.3px">Lorem ipsum</p><p class="t" style="font-size:2px">Lorem ipsum dolor sit amet, consectetuer adipiscing elit, sed diam nonummy nibh euismod tincidunt</p></div></div>
  </div>
  <div class="phone-frame" style="left:110px;top:20px;width:28px;height:56px"><p class="h5" style="font-size:3.4px">Lorem<br>ipsum dolor</p><svg class="ic o" width="7" height="7" style="margin:3px 0 2px"><use href="#i-book"/></svg><p class="t" style="font-size:1.8px">To introduce the students to the changing landscape of marketing and equip them with knowledge and tools needed to navigate the digital marketing world.</p></div>
  <div class="phone-frame" style="left:145px;top:37px;width:28px;height:56px"><p class="h5" style="font-size:3.4px">Dolor sit<br>amet, conse</p><svg class="ic o" width="7" height="7" style="margin:3px 0 2px"><use href="#i-gear"/></svg><p class="t" style="font-size:1.8px">You consider concepts and ideas in digital marketing as well as how to craft different tools and strategies to optimize your digital campaigns.</p></div>
  <div class="phone-frame" style="left:180px;top:54px;width:28px;height:56px"><p class="h5" style="font-size:3.4px">Consec</p><svg class="ic o" width="7" height="7" style="margin:6px auto 2px"><use href="#i-award"/></svg><p class="t" style="font-size:1.8px">You are required to take full ownership of the evaluation task to obtain the certificate. The evaluation task can be taken 3 times.</p></div>
  <div class="foot"><span>Copyright © 2025 Quillmere Partnership – All Rights Reserved.</span><span class="pg">20</span></div>
</section>

<section class="slide" style="left:280px;top:1037px" aria-label="Team members">
  <h2 class="heading"><b>Heading</b> Goes Here</h2>
  <div class="brand"><div class="mark"></div><div class="name">Quillmere<small>PARTNERSHIP</small></div></div>
  <div class="team-card" style="left:20px;top:35px"><div class="bar" style="background:var(--teal)"></div><div class="avatar" role="img" aria-label="Portrait photo of team member John Smith"></div><p class="h5">JOHN SMITH</p><p class="t" style="font-size:1.9px">Lorem ipsum dolor sit amet, consectetuer adipiscing elit, sed diam nonummy nibh euismod tincidunt ut laoreet dolore magna aliquam erat volutpat.</p></div>
  <div class="team-card" style="left:72px;top:35px"><div class="bar" style="background:var(--orange)"></div><div class="avatar" role="img" aria-label="Portrait photo of team member Millie Smith"></div><p class="h5 dk">MILLIE SMITH</p><p class="t" style="font-size:1.9px">Lorem ipsum dolor sit amet, consectetuer adipiscing elit, sed diam nonummy nibh euismod tincidunt ut laoreet dolore magna aliquam erat volutpat.</p></div>
  <div class="team-card" style="left:124px;top:35px"><div class="bar" style="background:var(--teal)"></div><div class="avatar" role="img" aria-label="Portrait photo of team member John Smith"></div><p class="h5">JOHN SMITH</p><p class="t" style="font-size:1.9px">Lorem ipsum dolor sit amet, consectetuer adipiscing elit, sed diam nonummy nibh euismod tincidunt ut laoreet dolore magna aliquam erat volutpat.</p></div>
  <div class="team-card" style="left:176px;top:35px"><div class="bar" style="background:var(--orange)"></div><div class="avatar" role="img" aria-label="Portrait photo of team member Millie Smith"></div><p class="h5 dk">MILLIE SMITH</p><p class="t" style="font-size:1.9px">Lorem ipsum dolor sit amet, consectetuer adipiscing elit, sed diam nonummy nibh euismod tincidunt ut laoreet dolore magna aliquam erat volutpat.</p></div>
  <div class="foot"><span>Copyright © 2025 Quillmere Partnership – All Rights Reserved.</span><span class="pg">21</span></div>
</section>

<section class="slide dark" style="left:522px;top:1037px" aria-label="Thank you">
  <div class="dark-photo" role="img" aria-label="Dark teal photo of a desk with documents behind the closing message"></div>
  <h2 style="left:118px;top:42px;font-size:15.5px;font-weight:800;line-height:1" class="w">Thank You</h2>
  <div class="contact" style="left:119px;top:64px">
    <svg width="6" height="6" viewBox="0 0 24 24"><path d="M6.6 10.8a15 15 0 0 0 6.6 6.6l2.2-2.2a1 1 0 0 1 1-.25 11.4 11.4 0 0 0 3.6.57 1 1 0 0 1 1 1V20a1 1 0 0 1-1 1A17 17 0 0 1 3 4a1 1 0 0 1 1-1h3.5a1 1 0 0 1 1 1c0 1.25.2 2.45.57 3.57a1 1 0 0 1-.25 1z" fill="#e8561c"/></svg>
    <span>+44 1632 960 418<br>+44 1632 960 418</span>
  </div>
  <div class="contact" style="left:119px;top:78px">
    <svg width="6" height="6" viewBox="0 0 24 24"><path d="M2 21 23 12 2 3v7l15 2-15 2z" fill="#e8561c"/></svg>
    <span>www.websitename.com<br>urname@email.com</span>
  </div>
  <div class="contact" style="left:119px;top:92px">
    <svg width="6" height="6" viewBox="0 0 24 24"><path d="M12 3 2 12h3v9h5v-6h4v6h5v-9h3z" fill="#e8561c"/></svg>
    <span>1234 Street name, town/city,<br>state/country, post/zip 012345.</span>
  </div>
</section>

</body>
</html>
```